FH banner

we need a banner design (36"x120" horizontal) that will be displayed on a local high school baseball field. My company ( Orbit Print Co) has been producing signage for the Fern Hollow community since 2009. We would like to communicate that we do more than banners. The final design should include the slogan "Signs Shirts Swag" and our Logo.

Target Market(s)

companies, teams, events, shirt and other marketing items.

Industry/Entity Type

Sign, Print,

Font styles to use
Sans Serif

Requirements
Should not have
• no baseball content.

```html
<!DOCTYPE html>
<html lang="en">
<head>
<meta charset="utf-8">
<title>Orbit Print Co – Fern Hollow Field Banner</title>
<link href="https://fonts.googleapis.com/css2?family=Oswald:wght@500;700&family=Roboto+Condensed:wght@800&display=swap" rel="stylesheet">
<style>
  :root {
    --page: #ffffff;
    --gold: #fcc419;
    --charcoal: #2b2b2b;
    --white: #ffffff;
  }
  * { margin: 0; padding: 0; box-sizing: border-box; }
  html, body { width: 1200px; height: 1200px; overflow: hidden; background: var(--page); }
  .canvas { position: relative; width: 1200px; height: 1200px; }
  .banner {
    position: absolute; left: 0; top: 127px; width: 1200px; height: 360px;
    background: var(--gold); overflow: hidden;
  }
  .banner__wave { position: absolute; inset: 0; width: 1200px; height: 360px; }
  .text { position: absolute; white-space: nowrap; line-height: 1; transform-origin: left top; }
  .headline {
    font-family: "Oswald", sans-serif; font-weight: 700; font-style: italic;
    letter-spacing: -1px;
  }
  .headline--lead {
    left: 252px; top: 16px; font-size: 38px; color: var(--charcoal);
    transform: scaleX(0.78) skewX(-6deg);
  }
  .headline--creative {
    left: 152px; top: 48px; font-size: 88px; color: var(--white);
    text-shadow: -3px 3px 0 var(--charcoal);
    transform: scaleX(0.9) skewX(-6deg);
  }
  .headline--beyond {
    left: 114px; top: 134px; font-size: 82px; color: var(--charcoal);
    text-shadow: -3px 3px 0 rgba(0,0,0,.3);
    transform: scaleX(0.68) skewX(-6deg);
  }
  .brand {
    position: absolute; left: 484px; top: 150px;
    display: flex; flex-direction: column; align-items: flex-start; gap: 4px;
  }
  .brand__row { display: flex; align-items: center; gap: 10px; }
  .brand__dot { width: 22px; height: 22px; border-radius: 50%; background: var(--charcoal); flex: none; }
  .brand__name {
    font-family: "Oswald", sans-serif; font-weight: 700; font-size: 38px;
    color: var(--charcoal); line-height: 1; white-space: nowrap;
  }
  .brand__established {
    margin-left: 32px; font-family: "Oswald", sans-serif; font-weight: 500;
    font-size: 17px; color: var(--charcoal); line-height: 1;
  }
  .impact__title {
    left: 702px; top: 28px; font-family: "Oswald", sans-serif; font-weight: 700;
    font-size: 46px; color: var(--white); letter-spacing: -1px;
    transform: scaleX(0.8);
  }
  .impact__body {
    left: 795px; top: 80px; font-family: "Oswald", sans-serif; font-weight: 700;
    font-size: 40px; line-height: 1.08; color: var(--charcoal); letter-spacing: -1px;
    transform: scaleX(0.88);
  }
  .slogan {
    left: 668px; top: 274px; font-family: "Roboto Condensed", sans-serif; font-weight: 800;
    font-size: 68px; color: var(--gold);
  }
  .website {
    left: 22px; top: 296px; font-family: "Roboto Condensed", sans-serif; font-weight: 800;
    font-size: 47px; color: var(--gold);
  }
</style>
</head>
<body>
<main class="canvas">
  <section class="banner" aria-label="Orbit Print Co field banner">
    <svg class="banner__wave" viewBox="0 0 1200 360" aria-hidden="true">
      <path d="M0 146 C 200 250, 400 295, 560 290 S 880 215, 1200 162 L1200 360 L0 360 Z" fill="#2b2b2b"/>
    </svg>

    <p class="text headline headline--lead">We're</p>
    <p class="text headline headline--creative">Creative</p>
    <p class="text headline headline--beyond">Beyond Banners</p>

    <div class="brand">
      <div class="brand__row">
        <span class="brand__dot"></span>
        <span class="brand__name">Orbit Print Co</span>
      </div>
      <span class="brand__established">Est. 2009</span>
    </div>

    <p class="text impact__title">Brand Impact:</p>
    <p class="text impact__body">Promotions That Make a<br>Lasting Impression!</p>

    <p class="text slogan">Signs Shirts Swag</p>
    <p class="text website">orbitprintco.com</p>
  </section>
</main>
</body>
</html>
```